Oral Surgeon Referral Pads

Hello. We need referral pads for Dr Loretta Pembrooke, DDS board certified oral surgeon's new office - Cedar Hollow Oral & Maxillofacial Surgery. See logo uploaded. See some images we would like included
Updates

Designs look the same

Font styles to use
Serif
Script

Colors
00AB8E
00BBA5
67D7C9
C6EFE9
E9F9F6

Requirements
Must have
• Color Pantone 623c. Also foldable business cards

```html
<!DOCTYPE html>
<html lang="en">
<head>
<meta charset="utf-8">
<title>Cedar Hollow Oral &amp; Maxillofacial Surgery – Referral Pad &amp; Cards</title>
<link rel="stylesheet" href="https://fonts.googleapis.com/css2?family=Arimo&family=Tinos:wght@400;700&family=Source+Sans+3&family=Alegreya+Sans:wght@400;500&display=swap">
<style>
  :root{
    --backdrop:#d1d1d1;
    --teal:#00ab8e;
    --teal-bright:#00bba5;
    --teal-soft:#67d7c9;
    --mint:#c6efe9;
    --mint-pale:#e9f9f6;
    --pantone-623:#a3d1c0;
    --paper:#ffffff;
    --ink:#4d4d4d;
    --rule:#555555;
  }
  *{margin:0;padding:0;box-sizing:border-box}
  html,body{width:1200px;height:1055px;overflow:hidden;background:var(--backdrop)}
  .canvas{position:relative;width:1200px;height:1055px}

  /* Referral pad sheet */
  .referral-pad{position:absolute;left:53px;top:122px;width:573px;height:810px;background:var(--paper);box-shadow:3px 3px 5px rgba(0,0,0,.25)}
  .referral-pad .base-band{position:absolute;left:0;bottom:0;width:100%;height:8px;background:var(--teal)}
  .brand{position:absolute;text-align:center;color:var(--teal)}
  .brand .mark{display:block;margin:0 auto;border-radius:50%;border:2px solid currentColor}
  .brand .name{font-family:"Tinos",serif;font-weight:400;display:block;white-space:nowrap;line-height:1}
  .brand .tagline{font-family:"Alegreya Sans",sans-serif;font-weight:500;display:block;white-space:nowrap;letter-spacing:.3px}
  .referral-pad .brand{left:40px;top:40px;width:180px}
  .referral-pad .brand .mark{width:32px;height:32px}
  .referral-pad .brand .name{font-size:27px;margin-top:12px}
  .referral-pad .brand .tagline{font-size:12px;margin-top:4px}

  .salutation{position:absolute;left:52px;top:250px;font-family:"Source Sans 3",sans-serif;font-size:12.5px;color:var(--ink)}
  .body-copy{position:absolute;left:51px;top:287px;width:472px;font-family:"Arimo",sans-serif;font-size:9.4px;line-height:11.8px;color:var(--ink)}
  .body-copy p{margin-bottom:10px}
  .closing{position:absolute;left:52px;top:534px;font-family:"Source Sans 3",sans-serif;font-size:7px;color:var(--ink)}
  .signature{position:absolute;left:54px;top:564px;width:86px;height:26px;background:var(--mint-pale);border-radius:3px}
  .footer{position:absolute;left:51px;top:753px;width:282px;font-family:"Tinos",serif;font-size:8.6px;color:var(--ink)}
  .footer .address{padding-bottom:3px;border-bottom:1px solid var(--rule)}
  .footer .contacts{display:flex;gap:6px;margin-top:5px;white-space:nowrap;align-items:center}
  .footer .contacts span{display:flex;align-items:center;gap:4px}
  .footer svg{width:7px;height:7px;fill:var(--teal)}

  /* Business cards */
  .card{position:absolute;left:662px;width:485px;background:var(--teal);box-shadow:3px 3px 5px rgba(0,0,0,.25)}
  .card-front{top:333px;height:277px}
  .card-front .brand{left:0;top:58px;width:100%;color:#fff}
  .card-front .brand .mark{width:58px;height:58px}
  .card-front .brand .name{font-size:44px;margin-top:16px}
  .card-front .brand .tagline{font-size:21px;margin-top:6px}

  .card-back{top:656px;height:277px;background:var(--paper)}
  .card-back .panel{position:absolute;left:0;top:0;width:100%;height:267px;background:var(--teal)}
  .card-back .brand{left:7px;top:25px;width:240px;color:#fff}
  .card-back .brand .mark{width:42px;height:42px}
  .card-back .brand .name{font-size:32px;margin-top:14px}
  .card-back .brand .tagline{font-size:15px;margin-top:4px}
  .card-back .holder{position:absolute;right:24px;top:26px;text-align:right;color:#fff;font-family:"Tinos",serif}
  .card-back .holder .person{font-size:16.5px;font-weight:700;letter-spacing:.3px}
  .card-back .holder .role{font-size:12.5px}
  .card-back .tab{position:absolute;right:0;top:28px;width:12px;height:28px;background:var(--paper)}
  .card-back .details{position:absolute;left:27px;top:151px;color:#fff;font-family:"Tinos",serif;font-size:13px;line-height:16.5px}
  .card-back .details .lines{margin-bottom:14px}
  .card-back .details .row{display:flex;align-items:center;gap:6px;line-height:17.5px}
  .card-back .details svg{width:10px;height:10px;fill:none;stroke:#fff;stroke-width:1.4}
</style>
</head>
<body>
<div class="canvas">

  <section class="referral-pad">
    <div class="brand">
      <span class="mark"></span>
      <span class="name">Cedar Hollow</span>
      <span class="tagline">Oral &amp; Maxillofacial Surgery</span>
    </div>

    <p class="salutation">Dear Dr. Whitby,</p>

    <div class="body-copy">
      <p>Thank you for referring your patient to our office. We have reviewed the enclosed records, radiographs and notes, and we will contact the patient within two business days to arrange a consultation. Please share any recent imaging, medical history updates or medication changes so our surgical team can plan care safely and in good time.</p>
      <p>Our practice offers wisdom tooth removal, dental implants, bone grafting, corrective jaw surgery and treatment of facial injuries. Each patient receives a full evaluation, a clear plan and an estimate before any procedure. We will keep you informed at each step and send a written report once the consultation is complete.</p>
      <p>For urgent cases, please call our office directly so we can see your patient the same day whenever possible. We accept most major insurance plans and will help patients understand their benefits before treatment begins. Post-operative instructions are given in writing, and our staff follows up by phone after every surgery to check on healing and comfort. After treatment, your patient will return to your care with a summary of the work completed and any follow-up needs.</p>
      <p>We value our partnership with your practice and look forward to caring for your patients. If you would like additional referral pads, appointment cards or patient brochures for your front desk, please let us know and we will send them promptly.</p>
    </div>

    <p class="closing">Sincerely,</p>
    <div class="signature" role="img" aria-label="Handwritten signature of the sender"></div>

    <div class="footer">
      <div class="address">Your address, city, state, ZIP 0000</div>
      <div class="contacts">
        <span><svg viewBox="0 0 10 10"><path d="M2 0.5l2 2-1 1.2c.6 1.3 1.6 2.3 2.9 2.9l1.2-1 2 2-1.3 1.6C4.2 9 1 5.8.4 1.9z"/></svg>555-014-2100</span>
        <span><svg viewBox="0 0 10 10"><path d="M0 2h10v6H0z M0 2l5 3.5L10 2"/></svg>hello@cedarhollowoms.com</span>
        <span><svg viewBox="0 0 10 10"><circle cx="5" cy="5" r="4.6"/></svg>www.cedarhollowoms.com</span>
      </div>
    </div>

    <div class="base-band"></div>
  </section>

  <section class="card card-front">
    <div class="brand">
      <span class="mark"></span>
      <span class="name">Cedar Hollow</span>
      <span class="tagline">Oral &amp; Maxillofacial Surgery</span>
    </div>
  </section>

  <section class="card card-back">
    <div class="panel"></div>
    <div class="brand">
      <span class="mark"></span>
      <span class="name">Cedar Hollow</span>
      <span class="tagline">Oral &amp; Maxillofacial Surgery</span>
    </div>
    <div class="holder">
      <div class="person">HARLAN WHITBY</div>
      <div class="role">Manager</div>
    </div>
    <div class="tab"></div>
    <div class="details">
      <div class="lines">Your Address<br>City, State, Zip 0000</div>
      <div class="row"><svg viewBox="0 0 10 10"><path d="M2 1l2 2-1 1.2c.6 1.3 1.6 2.3 2.9 2.9l1.2-1 2 2-1.3 1.3C4.2 9 1 5.8 .8 2.2z"/></svg>555-014-2100</div>
      <div class="row"><svg viewBox="0 0 10 10"><rect x=".8" y="2" width="8.4" height="6"/><path d="M.8 2l4.2 3.3L9.2 2"/></svg>hello@cedarhollowoms.com</div>
      <div class="row"><svg viewBox="0 0 10 10"><circle cx="5" cy="5" r="4.2"/><path d="M.8 5h8.4M5 .8c-2.4 2.6-2.4 5.8 0 8.4M5 .8c2.4 2.6 2.4 5.8 0 8.4"/></svg>www.cedarhollowoms.com</div>
    </div>
  </section>

</div>
</body>
</html>
```